ORLUq Business card. A.I. company developing trading strategies.

My name is tommaso fabbri and I'm CEO and co-founder of ORLUQ Research, an AI company focusing on generating Ai-driven trading strategies.
This is our website: https://orluq-research.example/
Values of our company: tech & R&D driven (we're all very mathy/stats/data driven), sophisticated (we only look for sophisticated, high knowledge investors), reserved (we don't go around telling anyone what we do).
Our main product: KobraFNX. A trading strategy that delivered 70% in 2022 and 20% in 2023 so far.
Our main potential clients: HNW individuals, hedge funds, asset managers, tech entrepreneur.
Hedge funds, asset managers, High Net Worth individuals, Pension funds
The basic: name, job title, company name, address, mail, phone number

```html
<!DOCTYPE html>
<html lang="en">
<head>
<meta charset="utf-8">
<title>ORLUq Research – Business Card</title>
<link rel="stylesheet" href="https://fonts.googleapis.com/css2?family=Lato:wght@400;700&display=swap">
<style>
  :root {
    --stage: #3b3b3b;
    --card: #1f1f20;
    --white: #ffffff;
    --grey: #c9c9c9;
    --red: #b0273a;
  }
  * { box-sizing: border-box; margin: 0; padding: 0; }
  html, body { width: 1200px; height: 689px; overflow: hidden; }
  body {
    background: var(--stage);
    font-family: "Lato", sans-serif;
    display: flex;
    align-items: center;
    justify-content: center;
    gap: 56px;
  }
  .card {
    width: 520px;
    height: 300px;
    background: var(--card);
    border-radius: 18px;
    position: relative;
    overflow: hidden;
    box-shadow: 0 18px 40px rgba(0,0,0,.35);
  }
  /* front */
  .card--front { display: flex; align-items: center; justify-content: center; }
  .wordmark { display: flex; align-items: center; gap: 14px; }
  .wordmark__dot { width: 12px; height: 12px; border-radius: 50%; background: var(--red); flex: none; }
  .wordmark__name {
    color: var(--white);
    font-weight: 400;
    font-size: 44px;
    letter-spacing: 5px;
    white-space: nowrap;
  }
  /* back */
  .card--back .wordmark { position: absolute; left: 40px; top: 42px; gap: 10px; }
  .card--back .wordmark__name { font-size: 26px; letter-spacing: 3px; }
  .card--back .wordmark__dot { width: 8px; height: 8px; }
  .holder { position: absolute; left: 40px; top: 118px; }
  .holder__name {
    color: var(--red);
    font-weight: 700;
    font-size: 24px;
    text-transform: uppercase;
    letter-spacing: .5px;
  }
  .holder__title { color: var(--grey); font-size: 15px; margin-top: 4px; }
  .contacts {
    position: absolute;
    left: 40px;
    top: 190px;
    list-style: none;
    color: var(--grey);
    font-size: 12.5px;
    line-height: 20px;
  }
  .contacts li { display: flex; align-items: center; gap: 10px; white-space: nowrap; }
  .contacts svg { width: 11px; height: 11px; fill: var(--red); flex: none; }
</style>
</head>
<body>
  <section class="card card--front">
    <div class="wordmark">
      <span class="wordmark__name">ORLUq Research</span>
      <span class="wordmark__dot"></span>
    </div>
  </section>

  <section class="card card--back">
    <div class="wordmark">
      <span class="wordmark__name">ORLUq Research</span>
      <span class="wordmark__dot"></span>
    </div>

    <div class="holder">
      <p class="holder__name">Tommaso Fabbri</p>
      <p class="holder__title">CEO &amp; Co-Founder</p>
    </div>

    <ul class="contacts">
      <li><svg viewBox="0 0 24 24" aria-hidden="true"><path d="M6.6 10.8a15 15 0 0 0 6.6 6.6l2.2-2.2a1 1 0 0 1 1-.25 11.4 11.4 0 0 0 3.6.57 1 1 0 0 1 1 1V20a1 1 0 0 1-1 1A17 17 0 0 1 3 4a1 1 0 0 1 1-1h3.5a1 1 0 0 1 1 1c0 1.25.2 2.45.57 3.57a1 1 0 0 1-.25 1z"/></svg>555019284</li>
      <li><svg viewBox="0 0 24 24" aria-hidden="true"><path d="M2 5h20v14H2zm2 2v.5l8 5 8-5V7z"/></svg>info@orluq-research.example</li>
      <li><svg viewBox="0 0 24 24" aria-hidden="true"><circle cx="12" cy="12" r="10"/></svg>orluq-research.example</li>
      <li><svg viewBox="0 0 24 24" aria-hidden="true"><path d="M12 2a7 7 0 0 0-7 7c0 5 7 13 7 13s7-8 7-13a7 7 0 0 0-7-7zm0 9.5a2.5 2.5 0 1 1 0-5 2.5 2.5 0 0 1 0 5z"/></svg>14 rue Vellane 75001 Paris</li>
    </ul>
  </section>
</body>
</html>
```